New Interrior Decoration company needs new website

We need a website for our new company specialising in interior decoration to residential and commercial markets.
We supply and install decorative and printed films for office and home decoration such as feature walls.
We would like to keep the design simple and clean.

Target Market(s)

Architects and interior designaers

Industry/Entity Type

It Company

Number of Pages Required

5+ page

Font styles to use
Sans Serif

Requirements
Must have
• Home page,
• Services/products page (split into commercial and residential)
• Gallery (split into commercial and residential)
• contact form and page
Nice to have
• Very clean and minimalistic design.

```html
<!DOCTYPE html>
<html lang="en">
<head>
<meta charset="utf-8">
<title>Vantage Interiors</title>
<link href="https://fonts.googleapis.com/css2?family=Roboto:wght@300;400;500;700&display=swap" rel="stylesheet">
<style>
:root{
  --blue:#1f5fbf;
  --blue-btn:#0d5cc2;
  --ink:#111;
  --white:#fff;
  --band:#2a2b2e;
  --band-dark:#1f2023;
  --footer:#2d2f33;
  --muted:#a9abb0;
  --line:#3d4045;
}
*{box-sizing:border-box;margin:0;padding:0}
html,body{width:1200px;height:2311px;overflow:hidden;background:var(--white);font-family:'Roboto',Arial,sans-serif}
.page{position:relative;width:1200px;height:2311px}
.abs{position:absolute}

.hero{left:0;top:0;width:1200px;height:632px;background:linear-gradient(180deg,#6e6c69 0%,#8d8a86 40%,#a19d98 70%,#5b5856 100%)}
.hero-shade{left:0;top:0;width:1200px;height:526px;background:radial-gradient(ellipse at 60% 60%,rgba(255,255,255,.18),rgba(0,0,0,.25))}
.nav{top:46px;left:96px}
.nav a{position:absolute;color:var(--white);font-size:20px;font-weight:500;text-decoration:none;white-space:nowrap}
.brand{left:0;width:1200px;top:150px;display:flex;justify-content:center;align-items:center;gap:10px}
.brand-mark{width:40px;height:40px;background:var(--blue-btn)}
.brand-name{font-size:34px;font-weight:700;color:var(--white);letter-spacing:-.5px;text-transform:uppercase;white-space:nowrap}
.hero-title{left:0;width:1200px;top:280px;text-align:center;color:var(--white);font-size:36px;font-weight:700}
.hero-sub{left:0;width:1200px;top:330px;text-align:center;color:var(--white);font-size:21px;letter-spacing:.4px;text-transform:uppercase}
.quote-band{left:0;top:526px;width:1200px;height:106px;background:rgba(30,30,32,.85)}
.quote-input{left:391px;top:551px;width:277px;height:44px;border:1px solid #555;background:#222;color:#ccc;font-size:13px;padding-left:22px;line-height:42px;white-space:nowrap}
.quote-btn{left:668px;top:551px;width:126px;height:44px;background:var(--blue-btn);color:var(--white);font-size:16px;font-weight:500;text-align:center;line-height:44px;white-space:nowrap}

.gallery-title{left:0;width:1200px;top:666px;text-align:center;color:var(--blue);font-size:28px;font-weight:300}
.tab{top:726px;width:160px;height:33px;line-height:33px;text-align:center;font-size:15px;font-weight:500;color:var(--white);border-radius:2px}
.tab-res{left:422px;background:var(--blue-btn)}
.tab-com{left:605px;background:#1b1b1b}

.card{width:250px}
.card-frame{width:250px;height:192px;background:var(--white);padding:10px;box-shadow:0 2px 12px rgba(0,0,0,.35)}
.card-photo{width:100%;height:100%}
.photo-res{background:linear-gradient(180deg,#6b6a3a 0%,#7a7845 60%,#9a9a68 80%,#5c5a30 100%)}
.photo-com{background:linear-gradient(160deg,#e8e8e6 0%,#b9b6b0 40%,#8a6e4e 65%,#3a332c 100%)}
.card-cat{margin:13px 0 0 8px;font-size:11px;color:var(--ink)}
.card-cat.res{color:var(--blue)}
.card-head{margin:14px 0 0 8px;font-size:13px;font-weight:700;color:var(--ink)}
.card-desc{margin:3px 0 0 8px;font-size:12px;line-height:15px;color:var(--blue);width:220px}

.pager{left:0;width:1200px;top:1822px;text-align:center;font-size:16px;color:var(--ink)}
.pager .on{color:var(--blue)}

.cta{left:0;top:1899px;width:1200px;height:94px;background:var(--band)}
.cta-text{left:295px;top:1928px;width:440px;color:var(--white);font-size:27px;font-weight:300;white-space:nowrap;line-height:34px}
.cta-btn{left:778px;top:1920px;width:143px;height:46px;background:var(--blue-btn);color:var(--white);font-size:17px;font-weight:500;text-align:center;line-height:46px;white-space:nowrap}

.footer{left:0;top:1993px;width:1200px;height:318px;background:var(--footer)}
.foot-brand{left:148px;top:2036px;display:flex;align-items:center;gap:8px}
.foot-brand .brand-mark{width:30px;height:30px}
.foot-brand .brand-name{font-size:22px}
.foot-about{left:148px;top:2086px;width:410px;font-size:12.5px;line-height:19px;color:var(--muted)}
.foot-copy{left:148px;top:2183px;font-size:12px;color:var(--muted);white-space:nowrap}
.foot-h{font-size:14px;font-weight:500;color:var(--white)}
.foot-contact{left:691px;top:2046px}
.foot-contact p{font-size:13px;color:#8a8d92;margin-top:10px;white-space:nowrap}
.foot-contact p+p{margin-top:6px}
.foot-follow{left:920px;top:2046px}
.social{display:flex;gap:14px;margin-top:12px}
.social span{width:11px;height:11px;border-radius:50%;background:#c9cbcf}
.foot-rule{left:148px;top:2240px;width:904px;height:1px;background:var(--line)}
.pay{left:148px;top:2264px;display:flex;gap:18px}
.pay span{width:42px;height:22px;background:#4a4d52;border-radius:3px}
.top-link{left:982px;top:2266px;font-size:13px;color:var(--white)}
.top-btn{left:1016px;top:2257px}
</style>
</head>
<body>
<div class="page">

  <header>
    <div class="abs hero" role="img" aria-label="Interior photo of a modern kitchen and dining room with pendant lights"></div>
    <div class="abs hero-shade"></div>
    <nav class="abs nav">
      <a style="left:0">About</a>
      <a style="left:87px">Services</a>
      <a style="left:197px">Gallery</a>
      <a style="left:287px">Contact</a>
    </nav>
    <div class="abs brand"><span class="brand-mark"></span><span class="brand-name">Vantage Interiors</span></div>
    <h1 class="abs hero-title">Stylish, Innovative Workmanship</h1>
    <p class="abs hero-sub">Symbol of extraordinary space and great design</p>
    <div class="abs quote-band"></div>
    <div class="abs quote-input">Enter your e-mail here</div>
    <div class="abs quote-btn">Quote Today</div>
  </header>

  <main>
    <h2 class="abs gallery-title">Our Gallery...... Our Showcase</h2>
    <div class="abs tab tab-res">Residential</div>
    <div class="abs tab tab-com">Commercial</div>

    <article class="abs card" style="left:185px;top:819px"><div class="card-frame"><div class="card-photo photo-res" role="img" aria-label="Residential feature wall with sideboard and framed print"></div></div><p class="card-cat res">Residential</p><h3 class="card-head">Heading here</h3><p class="card-desc">Some sort ofdescription here can be placed</p></article>
    <article class="abs card" style="left:472px;top:819px"><div class="card-frame"><div class="card-photo photo-com" role="img" aria-label="Commercial corridor with timber-clad curved wall"></div></div><p class="card-cat">Commercial</p><h3 class="card-head">Heading here</h3><p class="card-desc">Some sort ofdescription here can be placed</p></article>
    <article class="abs card" style="left:757px;top:819px"><div class="card-frame"><div class="card-photo photo-res" role="img" aria-label="Residential feature wall with sideboard and framed print"></div></div><p class="card-cat res">Residential</p><h3 class="card-head">Heading here</h3><p class="card-desc">Some sort ofdescription here can be placed</p></article>

    <article class="abs card" style="left:185px;top:1129px"><div class="card-frame"><div class="card-photo photo-res" role="img" aria-label="Residential feature wall with sideboard and framed print"></div></div><p class="card-cat res">Residential</p><h3 class="card-head">Heading here</h3><p class="card-desc">Some sort ofdescription here can be placed</p></article>
    <article class="abs card" style="left:472px;top:1129px"><div class="card-frame"><div class="card-photo photo-com" role="img" aria-label="Commercial corridor with timber-clad curved wall"></div></div><p class="card-cat">Commercial</p><h3 class="card-head">Heading here</h3><p class="card-desc">Some sort ofdescription here can be placed</p></article>
    <article class="abs card" style="left:757px;top:1129px"><div class="card-frame"><div class="card-photo photo-res" role="img" aria-label="Residential feature wall with sideboard and framed print"></div></div><p class="card-cat res">Residential</p><h3 class="card-head">Heading here</h3><p class="card-desc">Some sort ofdescription here can be placed</p></article>

    <article class="abs card" style="left:185px;top:1452px"><div class="card-frame"><div class="card-photo photo-res" role="img" aria-label="Residential feature wall with sideboard and framed print"></div></div><p class="card-cat res">Residential</p><h3 class="card-head">Heading here</h3><p class="card-desc">Some sort ofdescription here can be placed</p></article>
    <article class="abs card" style="left:472px;top:1452px"><div class="card-frame"><div class="card-photo photo-com" role="img" aria-label="Commercial corridor with timber-clad curved wall"></div></div><p class="card-cat">Commercial</p><h3 class="card-head">Heading here</h3><p class="card-desc">Some sort ofdescription here can be placed</p></article>
    <article class="abs card" style="left:757px;top:1452px"><div class="card-frame"><div class="card-photo photo-res" role="img" aria-label="Residential feature wall with sideboard and framed print"></div></div><p class="card-cat res">Residential</p><h3 class="card-head">Heading here</h3><p class="card-desc">Some sort ofdescription here can be placed</p></article>

    <p class="abs pager"><span class="on">1</span> | 2 | 3 | 4 | 5 | 6 | 7</p>

    <section>
      <div class="abs cta"></div>
      <svg class="abs" style="left:0;top:1899px" width="1200" height="94"><polygon points="690,0 1200,0 1200,94 718,94" fill="var(--band-dark)"/></svg>
      <p class="abs cta-text">Take a look at all what we offer you</p>
      <div class="abs cta-btn">Check it Out</div>
    </section>
  </main>

  <footer>
    <div class="abs footer"></div>
    <div class="abs foot-brand"><span class="brand-mark"></span><span class="brand-name">Vantage Interiors</span></div>
    <p class="abs foot-about">The Vantage Interiors team have over 20 years experience in the design, building, vinyl application and signage trades, giving us the ability to work through any creative or architectural needs your project may require.</p>
    <p class="abs foot-copy">© 2016 Vantage Interiors All rights reserved</p>
    <div class="abs foot-contact"><h4 class="foot-h">Contact Us</h4><p>info@vantageinteriors.example</p><p>02 5550 1234</p></div>
    <div class="abs foot-follow"><h4 class="foot-h">Follow Us</h4><div class="social"><span></span><span></span><span></span><span></span></div></div>
    <div class="abs foot-rule"></div>
    <div class="abs pay"><span></span><span></span><span></span><span></span><span></span><span></span></div>
    <span class="abs top-link">Top</span>
    <svg class="abs top-btn" width="36" height="36" viewBox="0 0 36 36"><circle cx="18" cy="18" r="17" fill="none" stroke="#c9cbcf" stroke-width="1.5"/><polyline points="12,21 18,15 24,21" fill="none" stroke="#fff" stroke-width="2"/></svg>
  </footer>

</div>
</body>
</html>
```